Halvern Aviation Group - "Coming Soon" Main Company Webpage

Design a main webpage that can be posted while a fully functional website is constructed. The design should be created to convey a sense of luxury and exclusivity. The main page should contain only one photo as the background. The photo I believe to show "luxury" and "Exclusivity" is listed as "Global Luxury Photo". I have included two other photos as well to aid in providing a variety of presentations.
The "Member PQTR" logo should appear somewhere on the main page but be less prevalent than the main company logo. "Coming Soon" should also appear to convey that a website is being constructed.
Tabs for the website:
- Aircraft Management
- Aircraft Sales
- Pilot Services
- Charter
- Flight Training

```html
<!DOCTYPE html>
<html lang="en">
<head>
<meta charset="utf-8">
<title>Halvern Aviation Group – Coming Soon</title>
<link rel="stylesheet" href="https://fonts.googleapis.com/css2?family=Montserrat:wght@400;500;600;700&display=swap">
<style>
:root{
  --blue:#0058a8;
  --blue-dark:#004a90;
  --navy:#0c1f3a;
  --ink:#111111;
  --text:#4a4a4a;
  --muted:#6b6b6b;
  --line:#d6d6d6;
  --page:#f4f4f4;
  --white:#ffffff;
}
*{box-sizing:border-box;margin:0;padding:0}
html,body{width:1200px;height:2778px;overflow:hidden;background:var(--page)}
body{font-family:'Montserrat',Arial,sans-serif;color:var(--text)}
.page{position:relative;width:1200px;height:2778px;overflow:hidden;background:var(--page)}
.abs{position:absolute}

/* header */
.hero-photo{position:absolute;left:0;top:0;width:1200px;height:560px;
  background:linear-gradient(100deg,#f1f1f1 0%,#e2e3e5 35%,#c9cbcf 60%,#9fa2a7 80%,#7d8086 100%)}
.hero-curve{position:absolute;left:0;top:500px;width:1200px;height:70px}
.social{position:absolute;display:flex;gap:7px}
.social span{width:30px;height:30px;border-radius:50%;border:1px solid #c4c4c4;display:block}
.social.light span{border-color:#7d8ca3;width:29px;height:29px;gap:8px}
.brand{position:absolute;text-align:center;color:var(--blue);font-weight:700;letter-spacing:1px}
.brand .name{display:block;font-size:28px;line-height:30px}
.brand .sub{display:block;font-size:14px;letter-spacing:3px;line-height:16px}
.contact-top{position:absolute;top:37px;font-size:14px;color:var(--ink);display:flex;align-items:center;gap:6px}
.contact-top svg{width:16px;height:16px}
.header-rule{position:absolute;left:120px;top:81px;width:959px;height:1px;background:#d4d4d4}
.header-sep{position:absolute;left:921px;top:22px;width:1px;height:46px;background:#d4d4d4}

/* hero */
.eyebrow{font-weight:600;letter-spacing:5px;font-size:16px;color:var(--ink)}
.hero-title{position:absolute;left:120px;top:196px;font-weight:700;font-size:47px;line-height:55px;color:var(--ink)}
.hero-title .hl{color:var(--blue)}
.hero-text{position:absolute;left:120px;top:323px;font-size:16px;line-height:21px;color:var(--ink);width:560px}
.btn{position:absolute;display:flex;align-items:center;justify-content:center;gap:10px;background:var(--blue);color:var(--white);
  font-weight:600;font-size:14px;letter-spacing:.3px;width:153px;height:40px;border-radius:2px}
.btn svg{width:22px;height:12px}

/* section titles */
.sec-title{position:absolute;left:0;width:1200px;text-align:center;font-weight:600;color:var(--blue);font-size:33px;line-height:36px}
.underline{position:absolute;left:572px;width:56px;height:2px;background:var(--ink)}
.lead{position:absolute;text-align:center;font-size:14px;line-height:21.6px;color:var(--text)}
.lead b{color:var(--ink);font-weight:600}

/* membership */
.about-rule{position:absolute;left:323px;top:791px;width:552px;height:1px;background:var(--line)}
.member{position:absolute;left:302px;top:822px;display:flex;align-items:flex-end;gap:10px}
.member .badge{width:40px;height:40px;border-radius:50%;background:var(--blue)}
.member .lbl{font-size:10px;color:var(--ink);line-height:12px}
.member .org{font-size:26px;font-weight:600;color:var(--ink);letter-spacing:3px;line-height:28px}
.member-text{position:absolute;left:497px;top:815px;width:385px;font-size:14.5px;line-height:18.5px;color:var(--ink)}

/* services */
.services{position:absolute;left:128px;top:1078px;width:968px;height:548px;background:var(--white);border-radius:22px;
  box-shadow:0 10px 30px rgba(0,0,0,.08);overflow:hidden}
.tabs{position:absolute;left:0;top:0;width:968px;height:75px;display:flex;background:#f0f0f0}
.tab{height:75px;display:flex;align-items:center;justify-content:center;font-size:14px;font-weight:600;color:var(--ink);
  letter-spacing:.3px;border-right:2px solid #fff}
.tab.active{background:var(--blue);color:var(--white)}
.tab-active-top{position:absolute;left:128px;top:1067px;width:261px;height:20px;background:var(--blue);border-radius:16px 4px 0 0}
.panel-title{position:absolute;left:90px;top:127px;font-size:26px;color:var(--ink);font-weight:400;letter-spacing:.5px}
.panel-title b{font-weight:700}
.panel-copy{position:absolute;left:90px;top:181px;width:770px;font-size:14px;line-height:21.6px;color:var(--text)}
.panel-copy p{margin-bottom:11px}

/* philosophy */
.band{position:absolute;left:0;top:1445px;width:1200px;height:483px;background:linear-gradient(180deg,var(--blue) 0%,var(--blue-dark) 100%)}
.white{color:var(--white)}

/* contact */
.info{position:absolute;left:258px;font-size:14px;line-height:22px;color:var(--text)}
.info .head{display:flex;align-items:center;gap:5px;color:var(--ink)}
.info .head svg{width:16px;height:16px}
.info strong{color:var(--ink);font-weight:600}
.form{position:absolute;left:529px;top:2108px;width:394px;height:386px;background:var(--white);border-radius:14px;box-shadow:0 10px 30px rgba(0,0,0,.08);z-index:3}
.field{position:absolute;left:34px;width:326px;font-size:14px;color:var(--text);border-bottom:1.5px solid var(--line)}

/* footer */
.footer{position:absolute;left:0;top:2420px;width:1200px;height:358px}
.copy{position:absolute;left:0;top:2727px;width:1200px;text-align:center;font-size:14px;color:#c8cfda}
</style>
</head>
<body>
<div class="page">

  <!-- hero -->
  <div class="hero-photo" role="img" aria-label="Close view of a private jet wing and engine against a cloudy grey sky"></div>
  <svg class="hero-curve" viewBox="0 0 1200 70" preserveAspectRatio="none" aria-hidden="true">
    <path d="M0 46 Q600 4 1200 46 L1200 70 L0 70 Z" fill="var(--page)"/>
  </svg>

  <div class="social" style="left:119px;top:31px"><span></span><span></span><span></span></div>
  <div class="brand" style="left:482px;top:26px;width:220px">
    <span class="name">HALVERN</span><span class="sub">AVIATION GROUP</span>
  </div>
  <div class="contact-top" style="left:779px">
    <svg viewBox="0 0 24 24" fill="none" stroke="var(--blue)" stroke-width="2"><path d="M5 3h4l2 5-2.5 1.5a11 11 0 005 5L15 12l5 2v4a2 2 0 01-2 2A16 16 0 013 5a2 2 0 012-2z"/></svg>
    (480) 555-0147
  </div>
  <div class="header-sep"></div>
  <div class="contact-top" style="left:939px">
    <svg viewBox="0 0 24 24" fill="none" stroke="var(--blue)" stroke-width="2"><rect x="3" y="5" width="18" height="14"/><path d="M3 5l9 8 9-8"/></svg>
    halvern.info@com
  </div>
  <div class="header-rule"></div>

  <div class="abs eyebrow" style="left:123px;top:171px">SOAR HIGHER</div>
  <h1 class="hero-title"><span class="hl">ELEVATE</span> YOUR<br>AVIATION EXPERIENCE</h1>
  <p class="hero-text">Discover Unparalleled Aircraft Management, Sales, Piloting, Charter, and Training Services for Your Journey Above the Clouds</p>
  <div class="btn" style="left:120px;top:401px">LAT'S TALK <svg viewBox="0 0 22 12" fill="none" stroke="#fff" stroke-width="1.8"><path d="M0 6h20M15 1l5 5-5 5"/></svg></div>

  <!-- about -->
  <h2 class="sec-title" style="top:604px">ABOUT US</h2>
  <div class="underline" style="top:655px"></div>
  <p class="lead" style="left:335px;top:677px;width:530px">At <b>Halvern Aviation Group</b>, we're your dedicated aviation partners. With services ranging from aircraft management and sales to piloting, charter, and training, we elevate your journey with unmatched expertise. Welcome to a world where the sky is just the beginning.</p>
  <div class="about-rule"></div>
  <div class="member">
    <span class="badge"></span>
    <div><div class="lbl">member of</div><div class="org">PQTR</div></div>
  </div>
  <p class="member-text">Our upcoming website, PQTR members, is about to take flight. Stay tuned for the launch of an unparalleled aviation experience.</p>

  <!-- services -->
  <h2 class="sec-title" style="top:980px">WHAT WE OFFER</h2>
  <div class="underline" style="top:1030px"></div>

  <div class="band"></div>
  <div class="tab-active-top"></div>
  <div class="services">
    <div class="tabs">
      <div class="tab active" style="width:261px">AIRCRAFT MANAGEMENT</div>
      <div class="tab" style="width:173px">AIRCRAFT SALES</div>
      <div class="tab" style="width:172px">PILOT SERVICES</div>
      <div class="tab" style="width:142px">CHARTER</div>
      <div class="tab" style="width:220px;border-right:0">FLIGHT TRAINING</div>
    </div>
    <h3 class="panel-title"><b>AIRCRAFT</b> MANAGEMENT</h3>
    <div class="panel-copy">
      <p>At Halvern Aviation Group, our Aircraft Management services go beyond the conventional. We understand that owning an aircraft involves more than just takeoffs and landings – it's about ensuring your investment remains impeccably maintained, consistently ready for flight, and compliant with industry regulations.</p>
      <p>With our dedicated team of experienced professionals, we take care of every detail. From scheduled maintenance and meticulous inspections to flight planning and crew coordination, our goal is to provide you with a worry-free ownership experience. We handle the complexities, so you can focus on the joy of flying.</p>
      <p>Whether you're a private owner, a corporation, or a fleet operator, our tailored solutions cater to your individual needs. Experience the convenience of having a team of experts working diligently to keep your aircraft in peak condition, maximizing its performance and value. Choose Halvern Aviation Group for aircraft management that truly takes you to new heights.</p>
    </div>
    <div class="btn" style="left:395px;top:458px">LAT'S TALK <svg viewBox="0 0 22 12" fill="none" stroke="#fff" stroke-width="1.8"><path d="M0 6h20M15 1l5 5-5 5"/></svg></div>
  </div>

  <!-- philosophy -->
  <div class="abs eyebrow white" style="left:0;width:1200px;text-align:center;top:1677px;font-size:14px">OUR PHILOSOPHY</div>
  <h2 class="sec-title white" style="top:1710px">AERONAUTICAL APPROACH</h2>
  <div class="underline" style="top:1767px;background:#fff"></div>
  <p class="lead white" style="left:265px;top:1783px;width:670px">At <b style="color:#fff">Halvern Aviation Group</b>, our aeronautical approach signifies a commitment to excellence, safety, and innovation. We believe in shaping the skies with unmatched expertise, ensuring every flight embodies the highest standards of aviation</p>

  <!-- contact -->
  <div class="abs eyebrow" style="left:0;width:1200px;text-align:center;top:1995px;font-size:14px">BE THE PART OF</div>
  <h2 class="sec-title" style="top:2026px">HALVERN AVIATION GROUP</h2>
  <div class="underline" style="top:2069px"></div>

  <div class="info" style="top:2146px">
    <div class="head"><svg viewBox="0 0 24 24" fill="none" stroke="var(--blue)" stroke-width="2"><path d="M12 22s7-7 7-12a7 7 0 00-14 0c0 5 7 12 7 12z"/><circle cx="12" cy="10" r="2.5"/></svg><strong>Halvern Aviation Group</strong></div>
    <div>1840 Larkspur Ave. Fairview,<br>Oregon 97024</div>
  </div>
  <div class="info" style="top:2247px">
    <div class="head"><svg viewBox="0 0 24 24" fill="none" stroke="var(--blue)" stroke-width="2"><path d="M5 3h4l2 5-2.5 1.5a11 11 0 005 5L15 12l5 2v4a2 2 0 01-2 2A16 16 0 013 5a2 2 0 012-2z"/></svg>Call Us</div>
    <strong>(480) 555-0147</strong>
  </div>
  <div class="info" style="top:2327px">
    <div class="head"><svg viewBox="0 0 24 24" fill="none" stroke="var(--blue)" stroke-width="2"><rect x="3" y="5" width="18" height="14"/><path d="M3 5l9 8 9-8"/></svg>Mail Us</div>
    <span style="color:var(--ink)">halvern.info@com</span>
  </div>

  <svg class="footer" viewBox="0 0 1200 358" preserveAspectRatio="none" aria-hidden="true">
    <path d="M0 18 Q600 -8 1200 18 L1200 358 L0 358 Z" fill="var(--navy)"/>
  </svg>

  <div class="form">
    <div class="field" style="top:29px;height:36px">Name:</div>
    <div class="field" style="top:93px;height:36px">Email:</div>
    <div class="field" style="top:157px;height:36px">Phone:</div>
    <div class="field" style="top:221px;height:80px">Message:</div>
    <div class="btn" style="left:121px;top:326px">LAT'S TALK <svg viewBox="0 0 22 12" fill="none" stroke="#fff" stroke-width="1.8"><path d="M0 6h20M15 1l5 5-5 5"/></svg></div>
  </div>

  <!-- footer -->
  <div class="brand" style="left:449px;top:2566px;width:300px">
    <span class="name" style="font-size:40px;line-height:42px">HALVERN</span><span class="sub" style="font-size:19px;line-height:22px">AVIATION GROUP</span>
  </div>
  <div class="social light" style="left:535px;top:2648px;gap:8px"><span></span><span></span><span></span></div>
  <div class="copy">© 2023 All Rights Reserved | Northwind Studio</div>

</div>
</body>
</html>
```